Frozen Yogurt Website

I need a new website based in Sydney Pelham Wharf. Our products are:

Frozen Yogurt
Smoothies
Organic Acai Bowls / Smoothies

we have professional photos of gourmet fruit and toppings in high resolution
we have the logo
we just need a web designer

no ecommerce required. Just promotional website:

following pages are needed:

About Us
Contact Us
Frozen Yogurt
Toppings
Smoothies
Acai Bowls

examples of websites we like:
http://www.velmorastreet.com
http://myplentifulpantry.com.au/
http://www.brumo.com.au

any questions please feel free to ask
Updates

Target Market(s)

healthy and organic food lovers
Frozen yogurt / desert eaters
tourist in pelham wharf

Industry/Entity Type

Promotional

Requirements
Should not have
• no ecommerce required

```html
<!DOCTYPE html>
<html lang="en">
<head>
<meta charset="utf-8">
<title>Yolumi – Frozen Yogurt, Pelham Wharf</title>
<link href="https://fonts.googleapis.com/css2?family=Roboto:wght@300;400;700&display=swap" rel="stylesheet">
<style>
:root{
  --wood-dark:#3f2c1c;
  --wood-mid:#6a4d33;
  --brown:#5f4529;
  --brown-deep:#573e25;
  --lime:#c5d63a;
  --lime-text:#c9d947;
  --orange:#ff5400;
  --white:#ffffff;
  --ink:#2a2a2a;
}
*{margin:0;padding:0;box-sizing:border-box}
html,body{width:1200px;height:1200px;overflow:hidden}
body{font-family:"Roboto",sans-serif;background:var(--brown);position:relative}
.hero{position:absolute;left:0;top:0;width:1200px;height:558px;
  background:radial-gradient(ellipse at 80% 35%,#a48866 0%,#7a5a3d 30%,var(--wood-mid) 55%,var(--wood-dark) 100%)}
.header{position:absolute;left:0;top:46px;width:1200px;height:57px;background:var(--white)}
.brand{position:absolute;left:120px;top:33px;width:90px;height:90px;border-radius:50%;background:var(--white);
  display:flex;align-items:center;justify-content:center;font-size:24px;font-weight:400;color:#3d3d3d}
.nav{position:absolute;right:130px;top:46px;height:57px;display:flex;align-items:center;font-size:14px;color:#222}
.nav span{white-space:nowrap}
.nav .sep{margin:0 13px;color:#444}
.promo{position:absolute;left:132px;top:176px;width:364px;height:364px;border-radius:50%;background:var(--orange)}
.promo-photo{position:absolute;left:195px;top:118px;width:235px;height:225px;border-radius:40% 40% 48% 48%;
  background:radial-gradient(circle at 50% 40%,#f4f4f4 0%,#d9d9d9 55%,rgba(200,200,200,0) 72%)}
.promo-text{position:absolute;left:190px;top:355px;width:250px;text-align:center;color:var(--white);
  font-weight:700;font-size:33px;line-height:34px}
.cta{position:absolute;left:466px;top:390px;width:252px;height:73px;background:var(--lime);
  display:flex;align-items:center;padding-left:24px;color:var(--white);font-size:20px;font-weight:400}
.cta svg{margin-left:14px}
.arrow{position:absolute;top:485px}
.welcome{position:absolute;left:0;top:558px;width:1200px;height:212px;background:var(--brown)}
.welcome h1{position:absolute;top:22px;left:0;width:1266px;text-align:center;font-weight:300;font-size:32px;color:var(--lime-text)}
.welcome p{position:absolute;left:129px;top:78px;width:941px;font-size:14px;line-height:24px;color:var(--white);
  text-align:justify;text-align-last:center;font-weight:300}
.menu{position:absolute;left:0;top:770px;width:1200px;height:337px;
  background:linear-gradient(#4e3620 0%,var(--brown-deep) 20%,var(--brown-deep) 100%)}
.menu h2{position:absolute;top:26px;width:1210px;text-align:center;font-weight:300;font-size:32px;color:var(--lime-text)}
.item{position:absolute;top:100px;width:180px;text-align:center}
.item .photo{width:160px;height:160px;margin:0 auto;border-radius:50%;
  background:radial-gradient(circle,#f5f0ea 0%,#d8cfc4 45%,rgba(120,90,60,0) 72%)}
.item .label{margin-top:18px;font-size:18px;color:var(--white);font-weight:300}
.footer{position:absolute;left:0;top:1107px;width:1200px;height:93px;background:var(--lime)}
.footer-nav{position:absolute;left:131px;top:23px;font-size:12px;color:var(--ink);display:flex}
.footer-nav .sep{margin:0 10px}
.copy{position:absolute;left:130px;top:55px;font-size:12px;color:var(--ink)}
.social{position:absolute;left:915px;top:35px;display:flex;gap:7px}
.social span{width:26px;height:26px;border-radius:50%;background:#1e1e1e;display:block}
</style>
</head>
<body>
<section class="hero" role="img" aria-label="Photo of a wooden table scattered with oats, dried cranberries, green apple slices, honey and a cup of tea"></section>

<header class="header"></header>
<div class="brand">yolumi</div>
<nav class="nav">
  <span>Home</span><span class="sep">|</span><span>About Us</span><span class="sep">|</span><span>Frozen Yogurt</span><span class="sep">|</span><span>Toppings</span><span class="sep">|</span><span>Smoothies</span><span class="sep">|</span><span>Acai Bowls</span><span class="sep">|</span><span>Contact Us</span>
</nav>

<div class="promo"></div>
<div class="promo-photo" role="img" aria-label="Two bowls of frozen yogurt topped with fresh fruit and berries"></div>
<div class="promo-text">Free Frozen<br>Yogurt<br>+<br>Toppings</div>
<div class="cta">Click Here For More
  <svg width="24" height="24" viewBox="0 0 24 24"><circle cx="12" cy="12" r="12" fill="#fff"/><path d="M10 7l5 5-5 5" fill="none" stroke="#c5d63a" stroke-width="2.5"/></svg>
</div>
<svg class="arrow" style="left:82px" width="40" height="56" viewBox="0 0 40 56"><path d="M34 2L6 28l28 26" fill="none" stroke="#ff5400" stroke-width="5"/></svg>
<svg class="arrow" style="left:1080px" width="40" height="56" viewBox="0 0 40 56"><path d="M6 2l28 26L6 54" fill="none" stroke="#ff5400" stroke-width="5"/></svg>

<section class="welcome">
  <h1>Welcome to Yolumi</h1>
  <p>Lorem Ipsum is simply dummy text of the printing and typesetting industry. Lorem Ipsum has been the industry's standard dummy text ever since the 1500s, when an unknown printer took a galley of type and scrambled it to make a type specimen book. It has survived not only five centuries, but also the leap into electronic typesetting, remaining essentially unchanged. It was popularised in the 1960s with the release of Typeline sheets containing Lorem Ipsum passages, and more recently with desktop publishing software like Pagecraft Desk including versions of Lorem Ipsum.</p>
</section>

<section class="menu">
  <h2>Our Menu</h2>
  <div class="item" style="left:188px"><div class="photo" role="img" aria-label="Frozen yogurt swirl in a white cup with berries"></div><div class="label">Frozen Yogurt</div></div>
  <div class="item" style="left:420px"><div class="photo" role="img" aria-label="Bowl of yogurt with fruit toppings"></div><div class="label">Toppings</div></div>
  <div class="item" style="left:685px"><div class="photo" role="img" aria-label="Mango smoothie in a cup with a straw"></div><div class="label">Smoothies</div></div>
  <div class="item" style="left:900px"><div class="photo" role="img" aria-label="White bowl of yogurt topped with strawberries"></div><div class="label">Acai Bowls</div></div>
</section>

<footer class="footer">
  <div class="footer-nav"><span>Home</span><span class="sep">|</span><span>About Us</span><span class="sep">|</span><span>Frozen Yogurt</span><span class="sep">|</span><span>Toppings</span><span class="sep">|</span><span>Smoothies</span><span class="sep">|</span><span>Acai Bowls</span><span class="sep">|</span><span>Contact Us</span></div>
  <div class="copy">Copyright© Birchline Studio All Rights Reserved</div>
  <div class="social"><span></span><span></span><span></span><span></span><span></span></div>
</footer>
</body>
</html>
```